Webpage for a treatment housing for young addicts.

I need a new design and files for my wordpress page. I need it to be more neat and clean. I need it to look professional with a starting page that will work as a navigation. I need like logo and 070-123 45 67 and such up top, a picture under it with one sentence as a slogan and under it 6 boxes to click to come to our different pages. Under it I want news etc.

Target Market(s)

Social services, employees and governements

Coding

Coded - Design and coding required

Font styles to use
Sans Serif

Colors
abd037
3176b5
9d9d9d
aaaaaa
f04a50

Requirements
Must have
• A nice design
Nice to have
• need it to look professional with a starting page that will work as a navigation. I need like logo and 070-123 45 67 and such up top, a picture under it with one sentence as a slogan and under it 6 boxes to click to come to our different pages. Under it I want news etc.
• today www.kolrev.se
• want more like www.tralvik.se or www.bersona.se
Should not have
• To many different colours and a messy design.

```html
<!DOCTYPE html>
<html lang="sv">
<head>
<meta charset="utf-8">
<title>Kolrev – Behandlingshem</title>
<link href="https://fonts.googleapis.com/css2?family=Open+Sans:wght@400;600;700;800&display=swap" rel="stylesheet">
<style>
:root{
  --green:#abd037;
  --blue:#3176b5;
  --grey:#9d9d9d;
  --grey-light:#aaaaaa;
  --red:#f04a50;
  --text:#4a4a4a;
  --bg-soft:#f2f3f4;
  --line:#e1e3e5;
  --white:#ffffff;
}
*{box-sizing:border-box;margin:0;padding:0}
html,body{width:688px;height:1200px;overflow:hidden}
body{font-family:"Open Sans",Arial,sans-serif;color:var(--text);background:var(--white);position:relative;font-size:7px;line-height:1.45}
.wrap{width:422px;margin:0 auto;position:relative}

/* top bar + header */
.topbar{height:14px;background:var(--white);border-bottom:1px solid var(--line)}
.topbar .wrap{display:flex;justify-content:flex-end;gap:12px;font-size:5.5px;color:var(--grey);line-height:14px}
.topbar span::before{content:"";display:inline-block;width:5px;height:5px;border-radius:50%;background:var(--green);margin-right:3px;vertical-align:-0.5px}
.header{height:44px;background:var(--white)}
.header .wrap{display:flex;align-items:center;justify-content:space-between;height:44px}
.brand{display:flex;align-items:center;gap:5px}
.brand-dot{width:18px;height:18px;border-radius:50%;background:var(--blue)}
.brand-name{font-weight:800;font-size:16px;color:var(--blue);letter-spacing:.3px}
.nav{display:flex;gap:13px;font-size:5.5px;font-weight:600;text-transform:uppercase;color:var(--grey)}
.nav .active{color:var(--blue);border-bottom:2px solid var(--green);padding-bottom:3px}

/* hero */
.hero{position:relative;height:182px;overflow:hidden}
.hero-photo{position:absolute;inset:0;background:linear-gradient(90deg,#6e8fa6 0%,#9fb1bd 32%,#c9cfd1 55%,#7d6a5e 72%,#3f3f45 100%)}
.hero-copy{position:absolute;left:133px;top:48px;width:200px;color:var(--white)}
.hero-title{font-size:13px;font-weight:800;line-height:1.15;text-transform:uppercase;letter-spacing:.2px}
.hero-text{font-size:5.5px;margin:7px 0 10px;opacity:.95}
.btn{display:inline-block;background:var(--blue);color:var(--white);font-size:5.5px;font-weight:700;text-transform:uppercase;padding:4px 11px;border-radius:2px}

/* page links */
.links{background:var(--bg-soft);padding:47px 0 26px}
.link-grid{display:grid;grid-template-columns:repeat(3,1fr);gap:9px 10px}
.link-box{background:var(--white);height:27px;border:1px solid var(--line);display:flex;align-items:center;justify-content:space-between;padding:0 8px;font-size:7px;font-weight:600;color:var(--text)}
.link-arrow{width:10px;height:10px}

/* news */
.news{padding:18px 0 20px}
.section-title{text-align:center;font-size:12px;font-weight:700;color:var(--text);display:flex;align-items:center;gap:10px;justify-content:center;margin-bottom:16px}
.section-title::before,.section-title::after{content:"";height:1px;width:120px;background:var(--line)}
.news-grid{display:grid;grid-template-columns:repeat(3,1fr);gap:14px 16px}
.news-item{display:flex;gap:7px;align-items:flex-start}
.news-date{flex:none;width:20px;height:20px;background:var(--blue);color:var(--white);font-size:5px;font-weight:700;text-align:center;line-height:1.1;padding-top:4px}
.news-text{font-size:5.5px;color:var(--grey);padding-top:2px}
.news-more{text-align:right;font-size:6px;color:var(--green);font-weight:600;margin-top:14px}

/* jobs */
.jobs{position:relative;height:230px;overflow:hidden}
.jobs-photo{position:absolute;inset:0;background:linear-gradient(90deg,#c9b8a4 0%,#ddd3c8 25%,#eceae6 50%,#a7b7a4 72%,#5f7a83 100%)}
.jobs-card{position:absolute;left:50%;top:20px;transform:translateX(-50%);width:248px;background:rgba(255,255,255,.9);padding:14px 20px 16px;text-align:center}
.jobs-card h2{font-size:12px;font-weight:700;color:var(--text);margin-bottom:8px}
.jobs-lead{font-size:6.5px;font-weight:700;color:var(--text);margin-bottom:7px;line-height:1.4}
.jobs-text{font-size:5.5px;color:var(--grey);text-align:left;margin-bottom:10px}

/* social */
.social{padding:16px 0 24px}
.social .section-title{margin-bottom:14px}
.social-row{display:flex;justify-content:center;gap:38px}
.social-item{width:100px;text-align:center}
.social-photo{width:96px;height:96px;border-radius:50%;margin:0 auto 8px;border:3px solid var(--white);box-shadow:0 0 0 1px var(--line)}
.p1{background:radial-gradient(circle at 50% 40%,#c79a7c,#5e4a3f)}
.p2{background:radial-gradient(circle at 50% 40%,#d9c5ad,#7f8c93)}
.p3{background:radial-gradient(circle at 50% 40%,#d8b79a,#6b5a4d)}
.social-item h3{font-size:7.5px;font-weight:700;color:var(--text)}
.social-item p{font-size:5.5px;color:var(--green);font-weight:600}

/* footer */
.footer{background:var(--bg-soft);border-top:1px solid var(--line);padding:18px 0 16px;height:140px}
.footer .wrap{display:grid;grid-template-columns:110px 70px 100px 1fr;gap:12px}
.footer .brand-name{font-size:14px}
.footer .brand-dot{width:15px;height:15px}
.footer-about{font-size:5px;color:var(--grey);margin-top:6px}
.footer h4{font-size:5.5px;font-weight:700;text-transform:uppercase;color:var(--text);margin-bottom:5px}
.footer ul{list-style:none;font-size:5.5px;color:var(--grey);line-height:1.8}
.footer address{font-style:normal;font-size:5.5px;color:var(--grey);line-height:1.8}
.subscribe{display:flex;margin:4px 0 8px}
.subscribe .field{flex:1;height:13px;background:var(--white);border:1px solid var(--line);font-size:5px;color:var(--grey-light);padding:2px 4px}
.subscribe .go{width:15px;height:13px;background:var(--green)}
.follow{display:flex;gap:4px}
.follow span{width:11px;height:11px;border-radius:50%;background:var(--white);border:1px solid var(--line)}
.copyright{position:absolute;left:0;right:0;bottom:0;height:20px;background:var(--white);border-top:1px solid var(--line);text-align:center;font-size:5px;color:var(--grey);line-height:20px}
</style>
</head>
<body>

<div class="topbar">
  <div class="wrap">
    <span>Mån – Fre 08–17</span>
    <span>070-123 45 67</span>
    <span>info@kolrev.se</span>
  </div>
</div>

<header class="header">
  <div class="wrap">
    <div class="brand"><span class="brand-dot"></span><span class="brand-name">Kolrev</span></div>
    <nav class="nav">
      <span class="active">Hem</span>
      <span>Om Kolrev</span>
      <span>Verksamheter</span>
      <span>Arbeta hos oss</span>
      <span>Kontakt</span>
    </nav>
  </div>
</header>

<section class="hero">
  <div class="hero-photo" role="img" aria-label="Foto: leende ung kvinna i ljus miljö"></div>
  <div class="hero-copy">
    <h1 class="hero-title">Vi skapar hållbara vägar till en bättre framtid</h1>
    <p class="hero-text">Vi ger unga med missbruk trygg vård, stöd och en ny start i livet.</p>
    <span class="btn">Läs mer</span>
  </div>
</section>

<section class="links">
  <div class="wrap link-grid">
    <div class="link-box">Kolrev<svg class="link-arrow" viewBox="0 0 10 10"><circle cx="5" cy="5" r="5" fill="#3176b5"/><path d="M4 3l2 2-2 2" stroke="#fff" stroke-width="1.2" fill="none"/></svg></div>
    <div class="link-box">Stödboende<svg class="link-arrow" viewBox="0 0 10 10"><circle cx="5" cy="5" r="5" fill="#3176b5"/><path d="M4 3l2 2-2 2" stroke="#fff" stroke-width="1.2" fill="none"/></svg></div>
    <div class="link-box">Uppdrag<svg class="link-arrow" viewBox="0 0 10 10"><circle cx="5" cy="5" r="5" fill="#3176b5"/><path d="M4 3l2 2-2 2" stroke="#fff" stroke-width="1.2" fill="none"/></svg></div>
    <div class="link-box">Vår Behandling<svg class="link-arrow" viewBox="0 0 10 10"><circle cx="5" cy="5" r="5" fill="#3176b5"/><path d="M4 3l2 2-2 2" stroke="#fff" stroke-width="1.2" fill="none"/></svg></div>
    <div class="link-box">Om Kolrev<svg class="link-arrow" viewBox="0 0 10 10"><circle cx="5" cy="5" r="5" fill="#3176b5"/><path d="M4 3l2 2-2 2" stroke="#fff" stroke-width="1.2" fill="none"/></svg></div>
    <div class="link-box">Placering<svg class="link-arrow" viewBox="0 0 10 10"><circle cx="5" cy="5" r="5" fill="#3176b5"/><path d="M4 3l2 2-2 2" stroke="#fff" stroke-width="1.2" fill="none"/></svg></div>
  </div>
</section>

<section class="news">
  <div class="wrap">
    <h2 class="section-title">Nyheter</h2>
    <div class="news-grid">
      <div class="news-item"><div class="news-date">12<br>MAJ</div><p class="news-text">Lorem ipsum dolor sit amet, consectetur adipiscing elit.</p></div>
      <div class="news-item"><div class="news-date">08<br>MAJ</div><p class="news-text">Lorem ipsum dolor sit amet, consectetur adipiscing elit.</p></div>
      <div class="news-item"><div class="news-date">02<br>MAJ</div><p class="news-text">Lorem ipsum dolor sit amet, consectetur adipiscing elit.</p></div>
      <div class="news-item"><div class="news-date">27<br>APR</div><p class="news-text">Lorem ipsum dolor sit amet, consectetur adipiscing elit.</p></div>
      <div class="news-item"><div class="news-date">19<br>APR</div><p class="news-text">Lorem ipsum dolor sit amet, consectetur adipiscing elit.</p></div>
      <div class="news-item"><div class="news-date">11<br>APR</div><p class="news-text">Lorem ipsum dolor sit amet, consectetur adipiscing elit.</p></div>
    </div>
    <p class="news-more">Nyhetsarkiv »</p>
  </div>
</section>

<section class="jobs">
  <div class="jobs-photo" role="img" aria-label="Foto: medarbetare i samtal, kvinna till vänster och man till höger"></div>
  <div class="jobs-card">
    <h2>Jobba hos oss</h2>
    <p class="jobs-lead">Looking forward to becoming part of a business in progress with the vision of being the best? Then you may want to look at our company.</p>
    <p class="jobs-text">We are constantly looking for new colleagues who share our values. We offer a warm team, good training and a chance to grow. Our work gives young people the support they need to build a new life, and every day matters. Send your application today and tell us a little about yourself and your experience.</p>
    <span class="btn">Läs mer</span>
  </div>
</section>

<section class="social">
  <div class="wrap">
    <h2 class="section-title">Kolrev i sociala medier</h2>
    <div class="social-row">
      <div class="social-item"><div class="social-photo p1" role="img" aria-label="Foto: porträtt av kvinna"></div><h3>Lorem ipsum dolor</h3><p>Inlägg</p></div>
      <div class="social-item"><div class="social-photo p2" role="img" aria-label="Foto: äldre kvinna i samtal"></div><h3>Lorem ipsum dolor</h3><p>Filmer</p></div>
      <div class="social-item"><div class="social-photo p3" role="img" aria-label="Foto: två kvinnor i samtal"></div><h3>Lorem ipsum dolor</h3><p>Nätverk</p></div>
    </div>
  </div>
</section>

<footer class="footer">
  <div class="wrap">
    <div>
      <div class="brand"><span class="brand-dot"></span><span class="brand-name">Kolrev</span></div>
      <p class="footer-about">Kolrev är ett behandlingshem för unga med missbruk. Vi erbjuder trygg vård, boende och stöd på vägen mot ett hållbart liv.</p>
    </div>
    <div>
      <h4>Snabblänkar</h4>
      <ul><li>Hem</li><li>Om oss</li><li>Behandling</li><li>Placering</li><li>Kontakt</li></ul>
    </div>
    <div>
      <h4>Hitta hit</h4>
      <address>Storgatan 12<br>123 45 Norrby<br>Tel: 070-123 45 67<br>info@kolrev.se</address>
    </div>
    <div>
      <h4>Prenumerera på vårt nyhetsbrev</h4>
      <div class="subscribe"><span class="field">Din e-post</span><span class="go"></span></div>
      <div class="follow"><span></span><span></span><span></span></div>
    </div>
  </div>
</footer>
<div class="copyright">Copyright © 2024 Kolrev. Alla rättigheter förbehållna · Integritet · Kontakt</div>

</body>
</html>
```